Book Cover for a technology book - The Silent Lattice

We are writing a book that is a handbook how to build a hybrid cloud - this is a technology concept where companies use cloud services both from the like of Vornix or Plenquor and also cloud services built in there own data centers - hence the term hybrid cloud. We want a book cover with the title - The Silent Lattice; which signifies that we will be teaching companies how to build a hybrid cloud that just works. We want the tagline - handbook for building Hybrid Clouds. The authors are Corwin Haddle and Ross Pelley. The cover is to be engaging and feel different than your usual technical manual. I don't have any graphics to help out however will be able to refine and tell you what I don and don't like based on your drafts. The book dimensions are yet to be determined, in the first instance it will be a PDF

Target Market(s)

technology executives and specialists

Industry/Entity Type

Information Technology

Colors

Designer to choose colors to be used in the design.

Requirements
Nice to have
• While I don't have a particular view to how it will look, I'd like the style to be more casual than ultra formal

```html
<!DOCTYPE html>
<html lang="en">
<head>
<meta charset="utf-8">
<title>The Silent Lattice — Handbook for Building Hybrid Clouds</title>
<link rel="stylesheet" href="https://fonts.googleapis.com/css2?family=Montserrat:ital,wght@0,400;0,800;1,800;1,900&display=swap">
<style>
  :root {
    --page: #ffffff;
    --cover-deep: #221d58;
    --cover-mid: #2a2668;
    --cover-glow: #332f7a;
    --ink-light: #ffffff;
    --art-core: #b9b6e6;
    --art-mid: #6d69bd;
    --art-edge: #3a3684;
    --art-accent: #4fd1c5;
  }
  html, body {
    margin: 0;
    padding: 0;
    width: 1200px;
    height: 1199px;
    overflow: hidden;
    background: var(--page);
  }
  .canvas {
    position: relative;
    width: 1200px;
    height: 1199px;
    background: var(--page);
  }
  .cover {
    position: absolute;
    left: 237px;
    top: 88px;
    width: 729px;
    height: 1027px;
    overflow: hidden;
    background:
      radial-gradient(ellipse at 15% 10%, var(--cover-glow) 0%, transparent 55%),
      linear-gradient(180deg, var(--cover-mid) 0%, var(--cover-deep) 100%);
    font-family: "Montserrat", sans-serif;
    color: var(--ink-light);
  }
  .title {
    position: absolute;
    left: 0;
    top: 58px;
    width: 100%;
    margin: 0;
    transform: rotate(-5deg);
    transform-origin: 50% 50%;
    text-align: center;
    font-weight: 900;
    font-style: italic;
    text-transform: uppercase;
    line-height: 1;
  }
  .title-lead {
    display: block;
    font-size: 82px;
    letter-spacing: -1px;
  }
  .title-main {
    display: block;
    font-size: 150px;
    letter-spacing: -4px;
    margin-top: 2px;
  }
  .hero-art {
    position: absolute;
    left: 81px;
    top: 336px;
    width: 600px;
    height: 320px;
    background:
      radial-gradient(ellipse 18% 42% at 50% 46%, var(--art-core) 0%, var(--art-mid) 70%, transparent 100%),
      radial-gradient(ellipse 12% 16% at 14% 50%, var(--art-mid) 0%, transparent 100%),
      radial-gradient(ellipse 12% 16% at 86% 50%, var(--art-mid) 0%, transparent 100%),
      radial-gradient(ellipse 40% 22% at 50% 78%, rgba(79, 209, 197, 0.35) 0%, transparent 100%),
      radial-gradient(ellipse 50% 50% at 50% 50%, var(--art-edge) 0%, transparent 100%);
  }
  .tagline {
    position: absolute;
    left: 0;
    top: 684px;
    width: 100%;
    margin: 0;
    text-align: center;
    font-weight: 900;
    font-style: italic;
    text-transform: uppercase;
    line-height: 1;
  }
  .tagline span { display: block; }
  .tagline-lead { font-size: 74px; letter-spacing: -1.5px; }
  .tagline-key { font-size: 98px; letter-spacing: -2px; margin-top: -2px; }
  .tagline-tail { font-size: 72px; letter-spacing: -1px; }
  .authors {
    position: absolute;
    left: 0;
    top: 950px;
    width: 100%;
    margin: 0;
    text-align: center;
    font-weight: 400;
    font-size: 29px;
    letter-spacing: 3px;
  }
</style>
</head>
<body>
<div class="canvas">
  <section class="cover">
    <h1 class="title">
      <span class="title-lead">The Silent</span>
      <span class="title-main">Lattice</span>
    </h1>
    <div class="hero-art" role="img" aria-label="Isometric illustration of a central server tower linked by glowing network lines to two laptops and two chips"></div>
    <h2 class="tagline">
      <span class="tagline-lead">Handbook for</span>
      <span class="tagline-key">Building</span>
      <span class="tagline-tail">Hybrid Clouds</span>
    </h2>
    <p class="authors">Corwin Haddle and Ross Pelley</p>
  </section>
</div>
</body>
</html>
```